THE POINT AT MAPLE SWALE HUDSON RIVER WATERFRONT LAND

crisp clear business cards on wood stock or thick paper with large font with a river otter logo, PERSONAL INFO ON ONE SIDE, PROJECT INFO ON THE OTHER SIDE
Updates

I don’t have a logo. Just thought that a photo of a river otter would look appealing.

Target Market(s)

Buyers and realtors

Industry/Entity Type

Real Estate Development

Contact Information for Business Card

MARTIN OSGOOD
518-730-4862 (Call or Text)
STONE HAVEN LLC PRINCIPAL

MOSHAVENRD@TARNMAIL.COM

Font styles to use
Sans Serif

Colors
fbfdfe
0792cd
00a990
fbed22
ec1f27

Requirements
Must have
• LARGE FONT, ROUNDED EDGES,
Nice to have
• ON THE BACK SIDE :
• THE POINT AT MAPLE SWALE
• HUDSON RIVER WATERFRONT LAND
• 2 TO 67 ACRES---READY TO BUILD
• PRICED TO SELL!

```html
<!DOCTYPE html>
<html lang="en">
<head>
<meta charset="utf-8">
<title>The Point at Maple Swale – Business Cards</title>
<link rel="stylesheet" href="https://fonts.googleapis.com/css2?family=Fira+Sans+Extra+Condensed:wght@700&display=swap">
<style>
  :root {
    --backdrop: #6c706e;
    --stock-light: #ecd7b8;
    --stock-mid: #e1c49c;
    --stock-deep: #d4b087;
    --ink: #4a2d1c;
    --emblem: #3f3f3d;
    --emblem-leaf: #4a3426;
  }
  * { margin: 0; padding: 0; box-sizing: border-box; }
  html, body {
    width: 1200px;
    height: 877px;
    overflow: hidden;
    background: var(--backdrop);
  }
  .sheet {
    position: relative;
    width: 1200px;
    height: 877px;
  }
  .card {
    position: absolute;
    top: 93px;
    width: 393px;
    height: 692px;
    border-radius: 34px;
    background: linear-gradient(170deg, var(--stock-light) 0%, var(--stock-mid) 55%, var(--stock-deep) 100%);
    font-family: "Fira Sans Extra Condensed", "Arial Narrow", sans-serif;
    font-weight: 700;
    color: var(--ink);
    text-align: center;
    text-transform: uppercase;
  }
  .card--project { left: 164px; }
  .card--contact { left: 645px; }

  .emblem-art {
    position: absolute;
    left: 72px;
    top: 58px;
    width: 250px;
    height: 292px;
  }

  .project-copy {
    position: absolute;
    left: 0;
    right: 0;
    top: 372px;
  }
  .project-name {
    font-size: 23px;
    line-height: 30px;
    letter-spacing: 0.2px;
  }
  .project-line {
    font-size: 49px;
    line-height: 49.5px;
    letter-spacing: 0.3px;
  }

  .contact-copy {
    position: absolute;
    left: 0;
    right: 0;
    top: 405px;
  }
  .contact-name {
    font-size: 48px;
    line-height: 56px;
    letter-spacing: 0.5px;
  }
  .contact-role {
    margin-top: 6px;
    font-size: 23px;
    line-height: 28px;
  }
  .contact-rule {
    width: 285px;
    height: 2px;
    margin: 22px auto 18px;
    background: var(--ink);
    opacity: 0.75;
  }
  .contact-phone {
    font-size: 51px;
    line-height: 58px;
    letter-spacing: 0.5px;
  }
  .contact-email {
    margin-top: 8px;
    font-size: 22px;
    line-height: 28px;
  }
</style>
</head>
<body>
<main class="sheet">

  <section class="card card--project" aria-label="Project side">
    <svg class="emblem-art" viewBox="0 0 250 292" role="img" aria-label="River otter on a riverbank beneath a leafy tree">
      <circle cx="125" cy="52" r="48" fill="var(--emblem-leaf)" opacity="0.85"/>
      <ellipse cx="125" cy="188" rx="123" ry="102" fill="var(--emblem)"/>
    </svg>
    <div class="project-copy">
      <p class="project-name">The Point at Maple Swale</p>
      <p class="project-line">Hudson River</p>
      <p class="project-line">Waterfront Land</p>
      <p class="project-line">2 to 67 Acres</p>
      <p class="project-line">Ready to Build</p>
      <p class="project-line">Priced to Sell!</p>
    </div>
  </section>

  <section class="card card--contact" aria-label="Contact side">
    <svg class="emblem-art" viewBox="0 0 250 292" role="img" aria-label="River otter on a riverbank beneath a leafy tree">
      <circle cx="160" cy="52" r="48" fill="var(--emblem-leaf)" opacity="0.85"/>
      <ellipse cx="125" cy="188" rx="123" ry="102" fill="var(--emblem)"/>
    </svg>
    <div class="contact-copy">
      <p class="contact-name">Martin Osgood</p>
      <p class="contact-role">Stone Haven LLC Principal</p>
      <div class="contact-rule"></div>
      <p class="contact-phone">518-730-4862</p>
      <p class="contact-email">moshavenrd@tarnmail.com</p>
    </div>
  </section>

</main>
</body>
</html>
```